Gewinnspielseite
Zielgruppe
Familen mit Kindern
Aufgabenstellung
Design für eine Gewinnspiel bei dem freier Eintritt für 1 Jahr in alle Freizeitparks in Deutschland verlost werden soll. Ablauf wäre das die Gewinnerfamilie uns den Eintrittsbeleg zusendet und wir diesen dann erstatten bis zu einer maximalen Höhe von 5.000 Euro.
Menüpunkte: Startseite, Teilnahmebedingungen, Preisdetails, Teilnehmen, Datenschutz.
Es soll eine Intro-Seite auf der der Preis groß heraus gestellt ist gestaltet werden mit den
entsprechenden Menüpunkten sowie eine Template-Seite in der wir dann alle notwendigen Inhalte einfügen können.
Gewinnspiel von uns finden Sie auf www.lostrommel-beispiel.de damit Sie sich ein Bild über die bisherigen Gewinnspiele machen können.
WICHTIG: Es soll nur die Eingangsseite und eine Template Seite erstellt werden. Die komplette Programmierung bzw. Füllung mit Inhalten wird von uns gemacht!

```html
<!DOCTYPE html>
<html lang="de">
<head>
<meta charset="utf-8">
<title>Parkfreude – Gewinnspiel</title>
<link rel="stylesheet" href="https://fonts.googleapis.com/css2?family=Arimo:wght@400;700&display=swap">
<style>
  :root {
    --page-bg: #ffffff;
    --column-bg: #fbfbfb;
    --text: #333333;
    --heading-blue: #2a8fce;
    --sky-top: #2f9de8;
    --sky-bottom: #7cc8f2;
    --hill-green: #7db21c;
    --wave-orange: #f5a623;
    --nav-bg: rgba(255,255,255,0.85);
    --nav-active: #f3efe6;
    --nav-border: #d8d8d8;
    --card-gray-1: #f4f4f4;
    --card-gray-2: #cfcfcf;
    --card-orange-1: #f7a126;
    --card-orange-2: #e07b0c;
    --card-green-1: #8ed83a;
    --card-green-2: #4ea51a;
    --card-blue-1: #3aa4ea;
    --card-blue-2: #1a7ac4;
    --footer-top: #e6e6e6;
    --footer-bottom: #cfcfcf;
    --footer-orange: #e58a12;
    --footer-green: #5aa51c;
  }
  * { box-sizing: border-box; margin: 0; padding: 0; }
  html, body { width: 1200px; height: 1030px; overflow: hidden; }
  body {
    background: var(--page-bg);
    font-family: "Arimo", Arial, sans-serif;
    color: var(--text);
    position: relative;
  }
  .page-column {
    position: absolute; left: 212px; top: 0; width: 761px; height: 1024px;
    background: var(--column-bg);
    box-shadow: 0 0 12px rgba(0,0,0,0.12);
  }
  .header-art { position: absolute; left: 200px; top: 0; width: 773px; height: 340px; }
  .balloons {
    position: absolute; left: 120px; top: 90px; width: 150px; height: 310px;
    background: linear-gradient(160deg, #8fd14f 0%, #2f7fe0 40%, #f0356e 75%, rgba(255,255,255,0) 100%);
    opacity: 0.55; border-radius: 60px 60px 20px 20px;
  }
  .brand {
    position: absolute; left: 320px; top: 78px;
    font-weight: 700; font-size: 46px; color: #ffffff; letter-spacing: 0.5px;
  }
  .main-nav {
    position: absolute; left: 262px; top: 256px; height: 43px;
    display: flex; background: var(--nav-bg);
  }
  .main-nav a {
    display: block; padding: 0 12px; line-height: 43px;
    font-size: 14.5px; color: #333; text-decoration: none;
    border-left: 1px solid var(--nav-border);
  }
  .main-nav a:first-child { border-left: none; }
  .main-nav a.is-highlight { background: var(--nav-active); }
  .content { position: absolute; left: 240px; top: 362px; width: 440px; }
  .content h1 { font-size: 20px; font-weight: 700; color: var(--heading-blue); margin-bottom: 14px; }
  .content p.lead { font-size: 17.5px; line-height: 19.7px; margin-bottom: 19.7px; }
  .content h2 { font-size: 15.5px; font-weight: 700; color: var(--heading-blue); margin: 11px 0 12px 1px; }
  .content p.small { font-size: 12px; line-height: 15px; margin-bottom: 15px; }
  .promo-card {
    position: absolute; border-radius: 9px; text-align: center;
    box-shadow: 2px 5px 8px rgba(0,0,0,0.3);
  }
  .prize-card {
    left: 697px; top: 408px; width: 305px; height: 108px; transform: rotate(-5deg);
    background: linear-gradient(var(--card-gray-1), var(--card-gray-2));
    padding-top: 16px;
  }
  .prize-card .title { color: var(--heading-blue); font-size: 20px; font-weight: 700; }
  .prize-card .detail { font-size: 15px; font-weight: 700; line-height: 18px; margin-top: 2px; }
  .send-card {
    left: 703px; top: 490px; width: 306px; height: 112px; transform: rotate(-6deg);
    background: linear-gradient(var(--card-orange-1), var(--card-orange-2));
    padding-top: 20px;
  }
  .send-card .detail { font-size: 19px; font-weight: 700; line-height: 23px; color: #2b2b2b; }
  .send-card .note { font-size: 14px; font-weight: 700; color: #fff; text-align: right; padding-right: 28px; margin-top: 2px; }
  .amount-card {
    left: 716px; top: 600px; width: 302px; height: 100px; transform: rotate(-4deg);
    background: linear-gradient(var(--card-green-1), var(--card-green-2));
  }
  .amount-card .upto { position: absolute; left: -4px; top: 2px; font-size: 17px; font-weight: 700; color: #222; }
  .amount-card .value { font-size: 62px; font-weight: 700; color: #fff; line-height: 74px; padding-top: 4px; }
  .amount-card .note { font-size: 14px; font-weight: 700; color: #222; margin-top: -2px; }
  .cta-card {
    left: 733px; top: 697px; width: 302px; height: 90px;
    background: linear-gradient(var(--card-blue-1), var(--card-blue-2));
    color: #fff; padding-top: 28px; text-decoration: none; display: block;
  }
  .cta-card .label { font-size: 19px; font-weight: 700; }
  .cta-card .sub { font-size: 13px; margin-top: 3px; }
  .site-footer {
    position: absolute; left: 212px; top: 903px; width: 761px; height: 121px;
    background: linear-gradient(var(--footer-top), var(--footer-bottom) 80%, #f0f0f0);
    font-size: 13px;
  }
  .footer-col { position: absolute; top: 16px; line-height: 17.5px; }
  .footer-col.left { left: 28px; }
  .footer-col.right { right: 28px; text-align: right; }
  .footer-col .title { margin-bottom: 17px; }
  .footer-col.left .title { color: var(--footer-orange); }
  .footer-col.right .title { color: var(--footer-green); }
  .imprint { position: absolute; left: 0; right: 0; top: 97px; text-align: center; color: #666; }
</style>
</head>
<body>
  <div class="page-column"></div>

  <svg class="header-art" viewBox="0 0 773 340" role="img" aria-label="Illustration: Freizeitpark mit Riesenrad, Achterbahn, Hügeln, Sonne und Wolken">
    <defs>
      <linearGradient id="sceneGradient" x1="0" y1="0" x2="0" y2="1">
        <stop offset="0" stop-color="var(--sky-top)"/>
        <stop offset="0.45" stop-color="var(--sky-bottom)"/>
        <stop offset="0.6" stop-color="var(--hill-green)"/>
        <stop offset="1" stop-color="var(--wave-orange)"/>
      </linearGradient>
    </defs>
    <path d="M40 0 H773 V120 C770 200 720 250 640 270 C500 300 330 250 230 300 C150 335 30 330 10 250 C0 180 20 90 40 0 Z" fill="url(#sceneGradient)"/>
  </svg>

  <div class="balloons" role="img" aria-label="Illustration: bunte Luftballons"></div>

  <div class="brand">Parkfreude</div>

  <nav class="main-nav">
    <a href="#">Startseite</a>
    <a href="#" class="is-highlight">Teilnahmebedingungen</a>
    <a href="#" class="is-highlight">Preisdetails</a>
    <a href="#">Teilnehmen</a>
    <a href="#">Datenschutz</a>
  </nav>

  <main class="content">
    <h1>Lorem ipsum dolor sit amend</h1>
    <p class="lead">Lorem ipsum dolor sit amend Lorem ipsum dolor sit amend<br>Lorem ipsum dolor sit amend Lorem ipsum dolor sit amend<br>Lorem ipsum dolor sit amend Lorem</p>
    <p class="lead">Lorem ipsum dolor sit amend Lorem ipsum dolor sit amend</p>
    <p class="lead">Lorem ipsum dolor sit amend Lorem ipsum dolor<br>Lorem ipsum dolor sit amend Lorem ipsum dolor sit<br>Lorem ipsum dolor sit amend Lorem ipsum dolor sit amend<br>Lorem ipsum dolor sit amend Lorem ipsum dolor sit<br>Lorem ipsum dolor sit amend Lorem ipsum dolor sit amend<br>Lorem ipsum dolor sit amend Lorem</p>
    <p class="lead">Lorem ipsum dolor sit amend Lorem ipsum dolor sit amend</p>
    <h2>Lorem ipsum dolor sit amend</h2>
    <p class="small">Lorem ipsum dolor sit amend Lorem ipsum dolor sit amend<br>Lorem ipsum dolor sit amend Lorem ipsum dolor sit<br>Lorem ipsum dolor sit amend Lorem ipsum</p>
    <p class="small">Lorem ipsum dolor sit amend Lorem ipsum</p>
    <p class="small">Lorem ipsum dolor sit amend Lorem ipsum dolor sit amend<br>Lorem ipsum dolor sit amend Lorem ipsum dolor sit amend<br>Lorem ipsum dolor sit amend Lorem ipsum dolor<br>Lorem ipsum dolor sit amend Lorem ipsum dolor sit amend</p>
  </main>

  <div class="promo-card prize-card">
    <div class="title">Gewinnen</div>
    <div class="detail">Sie 1 Jahr kostenlosen Eintritt<br>in alle Deutschen Freizeitparks</div>
  </div>
  <div class="promo-card send-card">
    <div class="detail">senden Sie uns<br>Ihren Einstrittsbeleg</div>
    <div class="note">und erhalten Sie</div>
  </div>
  <div class="promo-card amount-card">
    <div class="upto">bis zu</div>
    <div class="value">5000€</div>
    <div class="note">Rückerstattung Ihres Tickets</div>
  </div>
  <a class="promo-card cta-card" href="#">
    <div class="label">JETZT TEILNEHMEN !</div>
    <div class="sub">KLICKEN SIE HIER</div>
  </a>

  <footer class="site-footer">
    <div class="footer-col left">
      <div class="title">Lorem ipsum dolor sit amend</div>
      <div>Lorem ipsum dolor sit amend</div>
      <div>Lorem ipsum dolor sit amend</div>
      <div>Lorem ipsum dolor sit amend</div>
    </div>
    <div class="footer-col right">
      <div class="title">Lorem ipsum dolor sit amend</div>
      <div>Lorem ipsum dolor sit amend</div>
      <div>Lorem ipsum dolor sit amend</div>
      <div>Lorem ipsum dolor sit amend</div>
    </div>
    <div class="imprint">Impressum</div>
  </footer>
</body>
</html>
```